Flyer Design for a Boston Therapeutic Clinic

I am a body therapist who needs a couple of flyers designed:
1. To fit half a page.
2. To fit a 5 inch by 3.5 inch flyer.
My practice is based in Boston, MA and my web site is:
www.LarchTessvik.Com
For the First half page:
A. Have my company's name and color shown as it appears on my web site (Larch Tessvik)
B. Have the following text: "Control your weight (This part should be emphasized) by balancing your nervous and digestive system through the Tessvik Method. The Tessvik Method, a technique developed by Dr. Mara. Tessvik, uses physical pressure to manipulate visceral tissue to bring back resiliency and proper functioning of the whole body."
Also helps with
-Constipation
-Bloating
-IBS
-eating disorders and overeating
Our practitioner is highly experienced. Please visit our web sites for reviews.
C. I would like to have a nice earthy feeling, something that feels "freeing" like open flowers, or an open land scape such as mountains or fields.
D. I also like the color blue, white, orange; perhaps if these colors can be integrated into the flyer, that would be great.
E. "Visit our web site LarchTessvik.com or call 786-555-0148"
The Smaller Flyer :
A.The smaller Flyer should also have my Company's name as shown on my web site (Larch Tessvik)
B.The following text: " Restore your body's natural resiliency and greatly reduce your physical pain through the Dr. Mara Tessvik Method of Structural Integration."
C. "Our practitioner is highly experienced and has a great reputation; visit our web site for reviews."
"Benefits:
"reduce aches and pains
reduce joint pain
reduce chronic muscular tension"
D, "feel better after the first session!"
E. if you could use a picture of me working on someone from my web site, that would be great.
F. I also like the colors white, orange and silver, for this one.
G. "Visit our web site LarchTessvik.com or call 786-555 0148"
I am very open minded,
I would like the flyer to evoke a sense of tranquility, professionalism, and simplicity. So if you have another angle you think would look good, then go for it! As long as it looks clean, professional and helpful.
Thanks a lot!
If you need any pictures from my web site, I have the original high resolution files that i can send.
Professionals and working men and women from ages 20-70
Clinic

```html
<!DOCTYPE html>
<html lang="en">
<head>
<meta charset="utf-8">
<title>Larch Tessvik Therapy Flyers</title>
<link rel="stylesheet" href="https://fonts.googleapis.com/css2?family=Crimson+Pro:wght@300;400&family=Source+Sans+3:ital,wght@0,400;0,600;0,700;1,400&display=swap">
<style>
  :root {
    --page: #ffffff;
    --brand-orange: #c2461c;
    --cta-orange: #c4491e;
    --slate: #3c4147;
    --ink: #25282b;
    --body-grey: #4a4d50;
    --sky-top: #9fd3ec;
    --sky-mid: #d9eef8;
    --cloud: #f4f8fa;
    --hill: #5e6b35;
    --hill-dark: #3e4a22;
    --lake: #4d4a37;
    --silver-dark: #5a5a5a;
    --silver-light: #e6e6e6;
  }
  * { box-sizing: border-box; margin: 0; padding: 0; }
  html, body {
    width: 1200px; height: 582px; overflow: hidden;
    background: var(--page);
    font-family: "Source Sans 3", Arial, sans-serif;
  }
  .flyer { position: absolute; overflow: hidden; box-shadow: 0 0 3px rgba(0,0,0,.25); }

  /* Half-page flyer */
  .flyer-half { left: 15px; top: 22px; width: 768px; height: 545px; }
  .landscape-photo {
    position: absolute; inset: 0;
    background:
      linear-gradient(180deg, var(--sky-top) 0%, var(--sky-mid) 35%, var(--cloud) 55%, transparent 58%),
      linear-gradient(180deg, transparent 56%, var(--hill) 62%, var(--hill-dark) 80%, var(--lake) 88%, #3a3828 100%);
  }
  .flyer-half .brand-title {
    position: absolute; left: 90px; top: 56px;
    font-family: "Crimson Pro", Georgia, serif; font-weight: 300;
    font-size: 66px; line-height: 1; color: var(--slate); white-space: nowrap;
  }
  .brand-title .accent { color: var(--brand-orange); }
  .flyer-half .intro {
    position: absolute; left: 90px; top: 134px; width: 600px;
    font-size: 15px; line-height: 18px; color: var(--ink);
  }
  .intro strong { font-weight: 700; }
  .helps { position: absolute; left: 120px; top: 196px; font-size: 15px; line-height: 17px; color: var(--ink); }
  .helps h3 { font-size: 15px; font-weight: 700; margin-bottom: 2px; }
  .helps ul { list-style: none; }
  .experience {
    position: absolute; right: 90px; top: 226px; text-align: right;
    font-size: 17px; line-height: 20px; color: var(--ink);
  }
  .experience strong { color: var(--brand-orange); font-weight: 700; }
  .experience em { font-style: italic; }
  .cta {
    position: absolute; background: var(--cta-orange); color: #fff;
    text-align: center; white-space: nowrap;
  }
  .cta strong { font-weight: 700; }
  .flyer-half .cta { left: 149px; top: 489px; width: 469px; height: 30px; font-size: 17px; line-height: 30px; }

  /* Small flyer */
  .flyer-small { left: 803px; top: 22px; width: 382px; height: 545px;
    background: linear-gradient(180deg, #fafafa, #f0f0f0); }
  .session-photo {
    position: absolute; left: 0; top: 0; width: 382px; height: 260px;
    background: linear-gradient(180deg, var(--silver-dark) 0%, #9a9a9a 30%, var(--silver-light) 70%, rgba(240,240,240,0) 100%);
  }
  .flyer-small .brand-title {
    position: absolute; left: 37px; top: 188px;
    font-family: "Crimson Pro", Georgia, serif; font-weight: 300;
    font-size: 33px; line-height: 1; color: var(--slate); white-space: nowrap;
  }
  .flyer-small .intro {
    position: absolute; left: 37px; top: 236px; width: 320px;
    font-size: 14px; line-height: 17px; color: var(--body-grey);
  }
  .quote {
    position: absolute; left: 20px; width: 342px; top: 312px; text-align: center;
    font-style: italic; font-size: 13px; line-height: 14px; color: var(--brand-orange);
  }
  .benefits { position: absolute; left: 38px; top: 366px; font-size: 13px; line-height: 12.5px; color: var(--body-grey); }
  .benefits h3 { font-size: 13px; font-weight: 700; color: var(--ink); margin-bottom: 4px; }
  .benefits ul { list-style: none; }
  .promise {
    position: absolute; right: 48px; top: 468px;
    font-style: italic; font-size: 14px; color: var(--brand-orange);
  }
  .flyer-small .cta { left: 37px; top: 494px; width: 307px; height: 20px; font-size: 11px; line-height: 20px; }
</style>
</head>
<body>
  <section class="flyer flyer-half">
    <div class="landscape-photo" role="img" aria-label="Open landscape: blue sky with soft clouds above green mountains and a calm lake"></div>
    <h1 class="brand-title"><span class="accent">Larch</span> Tessvik Therapy</h1>
    <p class="intro"><strong>Control your weight</strong> by balancing your nervous and digestive system through the <em>Tessvik Method</em>. The Tessvik Method, a technique developed by <em>Dr. Mara. Tessvik</em>, uses physical pressure to manipulate visceral tissue to bring back resiliency and proper functioning of the whole body.</p>
    <div class="helps">
      <h3>Also helps with</h3>
      <ul>
        <li>- Constipation</li>
        <li>- Bloating</li>
        <li>- IBS</li>
        <li>- Eating disorders and overeating</li>
      </ul>
    </div>
    <p class="experience"><strong>Our practitioner is highly experienced.</strong><br><em>Please visit our websites for reviews.</em></p>
    <div class="cta">Visit our website <strong>LarchTessvik.com</strong> or call <strong>786-555-0148</strong></div>
  </section>

  <section class="flyer flyer-small">
    <div class="session-photo" role="img" aria-label="Black and white photo of the therapist working on a client's neck and shoulder"></div>
    <h2 class="brand-title"><span class="accent">Larch</span> Tessvik Therapy</h2>
    <p class="intro">Restore your body's natural resiliency and greatly reduce your physical pain through the <em>Dr. Mara Tessvik Method of Structural Integration.</em></p>
    <p class="quote">"Our practitioner is highly experienced and has a great reputation; visit our web site for reviews.</p>
    <div class="benefits">
      <h3>Benefits:</h3>
      <ul>
        <li>reduce aches and pains</li>
        <li>reduce joint pain</li>
        <li>reduce chronic muscular tension</li>
      </ul>
    </div>
    <p class="promise">feel better after the first session!</p>
    <div class="cta">Visit our website <strong>LarchTessvik.com</strong> or call <strong>786-555-0148</strong></div>
  </section>
</body>
</html>
```